Ad to be used on social media.

____________________________________________________________________________

Bored at Home?

Study to become a
Virtual Mortgage Originator today...

Complete 20 Hour Online Course & State Exam
in 30 days or less

Earn $3,000 to $5,000 on average per loan
No Work Hours, Goals or Quotas
Full Time or Part Time Opportunities

Email us at employment@brightlanehome.com

Oakmere Lending Group, Inc.
7200 Wexbury Lane
Ellicott City, MD 21043
(800) 461-9027
www.brightlanehome.com
NMLS #738160

```html
<!DOCTYPE html>
<html lang="en">
<head>
<meta charset="utf-8">
<title>Bored at Home? – Oakmere Lending Group</title>
<link rel="stylesheet" href="https://fonts.googleapis.com/css2?family=Fjalla+One&family=Oswald:wght@300;400&family=Open+Sans:wght@700;800&display=swap">
<style>
  :root {
    --blue: #0b5aa6;
    --blue-soft: #8fb3d6;
    --olive: #a99a2b;
    --white: #ffffff;
    --photo-light: #eae6e1;
    --photo-mid: #c9b8a8;
  }
  html, body { margin: 0; padding: 0; overflow: hidden; background: var(--white); }
  .ad {
    position: relative; width: 927px; height: 1200px; overflow: hidden;
    background: var(--white); font-family: "Open Sans", sans-serif;
  }
  .ad__shapes { position: absolute; inset: 0; }
  .ad__photo { position: absolute; }
  .brand {
    position: absolute; left: 110px; top: 60px; width: 310px; text-align: center;
    font-family: "Open Sans", sans-serif; font-weight: 700; font-size: 22px;
    line-height: 1.25; color: var(--blue);
  }
  .headline {
    position: absolute; left: 44px; top: 270px; margin: 0;
    font-family: "Fjalla One", sans-serif; font-weight: 400; font-size: 86px;
    line-height: 0.95; color: var(--white); letter-spacing: 0.5px;
  }
  .subhead {
    position: absolute; left: 44px; top: 450px; margin: 0; padding-left: 10px;
    border-left: 2px solid var(--white);
    font-weight: 700; font-size: 28px; line-height: 1.22; color: var(--white);
  }
  .badge {
    position: absolute; left: 565px; top: 347px; width: 280px; height: 280px;
    display: flex; flex-direction: column; align-items: center; justify-content: center;
    text-align: center;
  }
  .badge__title { font-weight: 800; font-size: 39px; line-height: 1.1; color: var(--blue); }
  .badge__rule { width: 52px; height: 3px; background: var(--olive); margin: 8px 0 10px; }
  .badge__detail { font-weight: 700; font-size: 24px; line-height: 1.1; color: var(--olive); }
  .earn {
    position: absolute; left: 488px; top: 690px; margin: 0; padding-left: 8px;
    border-left: 3px solid var(--white);
    font-weight: 700; font-size: 58px; line-height: 0.92; color: var(--white);
  }
  .earn__note {
    position: absolute; left: 488px; top: 808px; margin: 0;
    font-weight: 700; font-size: 24px; color: var(--white);
  }
  .perks {
    position: absolute; left: 476px; top: 853px; width: 372px; height: 72px;
    box-sizing: border-box; padding: 8px 14px; background: var(--white); border-radius: 14px;
  }
  .perks__lead { font-family: "Fjalla One", sans-serif; font-size: 21px; line-height: 1.1; color: var(--olive); }
  .perks__line { font-family: "Oswald", sans-serif; font-weight: 400; font-size: 24px; line-height: 1.15; color: var(--blue); }
  .email__label {
    position: absolute; left: 128px; top: 1045px; width: 265px;
    display: flex; align-items: center; gap: 10px;
    font-weight: 700; font-size: 26px; color: var(--olive); white-space: nowrap;
  }
  .email__label::before, .email__label::after { content: ""; flex: 1; height: 3px; background: var(--blue); }
  .email__address {
    position: absolute; left: 30px; top: 1075px; width: 459px; height: 84px;
    display: flex; align-items: center; justify-content: center;
    font-family: "Oswald", sans-serif; font-weight: 300; font-size: 31px; color: var(--white);
  }
  .divider { position: absolute; left: 500px; top: 997px; width: 1px; height: 180px; background: var(--blue); }
  .contact {
    position: absolute; left: 526px; top: 998px; margin: 0; padding: 0; list-style: none;
    font-weight: 700; font-size: 25px; line-height: 1.13; color: var(--blue);
  }
  .contact li { display: flex; align-items: flex-start; gap: 4px; }
  .contact svg { flex: none; margin-top: 4px; }
  .contact .contact__indent { padding-left: 22px; }
  .nmls {
    position: absolute; left: 551px; top: 1126px; width: 202px; height: 44px;
    display: flex; align-items: center; justify-content: center;
    background: var(--olive); font-weight: 700; font-size: 24px; color: var(--white);
  }
</style>
</head>
<body>
<div class="ad">
  <svg class="ad__photo" width="927" height="560" style="left:0;top:0" role="img" aria-label="Photo of a young woman lying on a sofa holding a TV remote, looking bored">
    <defs>
      <linearGradient id="photoTone" x1="0" y1="0" x2="1" y2="1">
        <stop offset="0" stop-color="var(--photo-light)"/>
        <stop offset="1" stop-color="var(--photo-mid)"/>
      </linearGradient>
    </defs>
    <rect width="927" height="560" fill="url(#photoTone)"/>
  </svg>

  <svg class="ad__shapes" width="927" height="1200" viewBox="0 0 927 1200" aria-hidden="true">
    <path d="M0 0 H420 C430 230 520 420 927 470 V668 C700 690 450 560 0 555 Z" fill="var(--blue)"/>
    <path d="M0 540 C300 510 620 690 927 655 V965 C620 990 320 930 0 913 Z" fill="var(--olive)"/>
    <path d="M0 925 C200 935 400 965 560 980" fill="none" stroke="var(--blue)" stroke-width="2"/>
    <circle cx="265" cy="75" r="158" fill="var(--white)"/>
    <circle cx="705" cy="487" r="153" fill="var(--blue-soft)"/>
    <circle cx="705" cy="487" r="140" fill="var(--white)"/>
    <circle cx="218" cy="746" r="177" fill="var(--white)"/>
    <path d="M30 1090 L489 1075 L478 1159 L30 1159 Z" fill="var(--blue)"/>
  </svg>

  <svg class="ad__photo" width="336" height="336" style="left:50px;top:578px" role="img" aria-label="Photo of a smiling woman working on a laptop by a window">
    <defs>
      <linearGradient id="workTone" x1="0" y1="0" x2="1" y2="1">
        <stop offset="0" stop-color="#5d5a58"/>
        <stop offset="0.6" stop-color="#b9bcbf"/>
        <stop offset="1" stop-color="#e6e4df"/>
      </linearGradient>
    </defs>
    <circle cx="168" cy="168" r="168" fill="url(#workTone)"/>
  </svg>

  <div class="brand">Oakmere Lending Group, Inc.</div>

  <h1 class="headline">BORED AT<br>HOME?</h1>
  <p class="subhead">Study to become a virtual<br>Mortgage originator today...</p>

  <div class="badge">
    <div class="badge__title">Complete<br>20 Hour</div>
    <div class="badge__rule"></div>
    <div class="badge__detail">Online Course &amp;<br>State Exam<br>in 30 days or<br>less</div>
  </div>

  <p class="earn">EARN $3,000<br>TO $5,000</p>
  <p class="earn__note">on average per loan</p>
  <div class="perks">
    <div class="perks__lead">No Work Hours, Goals or Quotas</div>
    <div class="perks__line">Full Time or Part Time Opportunities</div>
  </div>

  <div class="email__label">Email us at</div>
  <div class="email__address">employment@brightlanehome.com</div>

  <div class="divider"></div>
  <ul class="contact">
    <li><svg width="18" height="22" viewBox="0 0 18 22" aria-hidden="true"><path d="M9 1a7 7 0 0 0-7 7c0 5 7 13 7 13s7-8 7-13a7 7 0 0 0-7-7z" fill="var(--olive)"/><circle cx="9" cy="8" r="2.6" fill="var(--white)"/></svg>7200 Wexbury Lane</li>
    <li class="contact__indent">Ellicott City, MD 21043</li>
    <li><svg width="18" height="20" viewBox="0 0 18 18" aria-hidden="true"><path d="M4 2l3 3-1.5 2a9 9 0 0 0 5.5 5.5L13 11l3 3-2 2C8 16 2 10 2 4z" fill="var(--olive)"/></svg>(800) 461-9027</li>
    <li><svg width="18" height="20" viewBox="0 0 18 18" aria-hidden="true"><g fill="none" stroke="var(--olive)" stroke-width="1.5"><circle cx="9" cy="9" r="7"/><ellipse cx="9" cy="9" rx="3" ry="7"/><path d="M2 9h14M3.5 5h11M3.5 13h11"/></g></svg>www.brightlanehome.com</li>
  </ul>
  <div class="nmls">NMLS #738160</div>
</div>
</body>
</html>
```